Used Car Dealer seeks an Amazing Business Card Design

We are looking for a business card design that incorporates our logo and grabs the attention of anyone we give the business card to.

Looking to use the same colors as the logo. Our Logo choice is the black background with Red and Silver/Grey Lettering.

We also would like to see some embossed designs.

Target Market(s)

Used Car Buyers, Automotive, Auto

Industry/Entity Type

Automotive

Contact Information for Business Card

BVEL7K
Gordon Whitlock
482 Tarrow Lane
Suite 207
Corvane, GA 30199
Office (770) 555-0142
Cell (770) 555-0187
bvel7kga@quellmail.com
www.bvel7kga.com

Colors
ffffff
ee3036

Requirements
Must have
• Must include our logo (Black Background with Red and Silver/Grey Lettering)
Nice to have
• Embossed Design. Can be Single or Double Sided.

```html
<!DOCTYPE html>
<html lang="en">
<head>
<meta charset="utf-8">
<title>BVEL7K Business Card</title>
<link href="https://fonts.googleapis.com/css2?family=Open+Sans:wght@400;600;700&display=swap" rel="stylesheet">
<style>
  :root {
    --stage: #3a3431;
    --card: #141414;
    --card-edge: #0c0c0c;
    --red: #ee3036;
    --white: #ffffff;
    --muted: #c8c8c8;
  }
  * { box-sizing: border-box; margin: 0; padding: 0; }
  html, body {
    width: 1200px;
    height: 844px;
    overflow: hidden;
    background: var(--stage);
    font-family: "Open Sans", Arial, sans-serif;
  }
  .canvas {
    position: relative;
    width: 1200px;
    height: 844px;
  }
  .card {
    position: absolute;
    top: 262px;
    width: 540px;
    height: 320px;
    background: radial-gradient(ellipse at 50% 35%, #1d1d1d 0%, var(--card) 60%, var(--card-edge) 100%);
    box-shadow: 0 14px 30px rgba(0,0,0,0.55);
    overflow: hidden;
  }
  .card--front { left: 45px; }
  .card--back { left: 615px; }

  .brand {
    position: absolute;
    display: flex;
    align-items: center;
    gap: 12px;
  }
  .brand__dot {
    width: 14px;
    height: 14px;
    border-radius: 50%;
    background: var(--red);
  }
  .brand__name {
    font-weight: 700;
    font-size: 46px;
    letter-spacing: 1px;
    color: var(--red);
    line-height: 1;
  }
  .card--front .brand { left: 120px; top: 70px; }
  .card--back .brand { left: 50%; top: 112px; transform: translateX(-50%); }

  .contact {
    position: absolute;
    right: 28px;
    top: 128px;
    list-style: none;
    text-align: right;
  }
  .contact__item {
    display: flex;
    justify-content: flex-end;
    align-items: center;
    gap: 9px;
    font-size: 12.5px;
    line-height: 21px;
    color: var(--white);
  }
  .contact__icon { width: 10px; height: 10px; flex: none; }

  .person {
    position: absolute;
    left: 32px;
    top: 200px;
  }
  .person__name {
    font-weight: 600;
    font-size: 17px;
    line-height: 24px;
    color: var(--red);
    margin-bottom: 6px;
  }
  .person__address {
    font-style: normal;
    font-size: 13.5px;
    line-height: 21px;
    color: var(--muted);
    padding-left: 18px;
  }

  .website {
    position: absolute;
    right: 150px;
    top: 198px;
    font-size: 11.5px;
    color: var(--white);
  }
</style>
</head>
<body>
<main class="canvas">

  <section class="card card--front" aria-label="Business card front">
    <div class="brand">
      <span class="brand__dot"></span>
      <span class="brand__name">BVEL7K</span>
    </div>

    <ul class="contact">
      <li class="contact__item">(770) 555-0142
        <svg class="contact__icon" viewBox="0 0 10 10" aria-hidden="true"><path d="M2 1l2 2-1 1.3c.6 1.2 1.5 2.1 2.7 2.7L7 6l2 2-1.3 1.5C4.5 9.2.8 5.5.5 2.3z" fill="#ee3036"/></svg>
      </li>
      <li class="contact__item">(770) 555-0187
        <svg class="contact__icon" viewBox="0 0 10 10" aria-hidden="true"><rect x="2" y=".5" width="6" height="9" rx="1" fill="none" stroke="#ee3036" stroke-width="1.2"/></svg>
      </li>
      <li class="contact__item">bvel7kga@quellmail.com
        <svg class="contact__icon" viewBox="0 0 10 10" aria-hidden="true"><rect x=".5" y="2" width="9" height="6.5" fill="#ee3036"/><path d="M.8 2.3L5 5.6l4.2-3.3" fill="none" stroke="#141414" stroke-width="1"/></svg>
      </li>
      <li class="contact__item">www.bvel7kga.com
        <svg class="contact__icon" viewBox="0 0 10 10" aria-hidden="true"><circle cx="5" cy="5" r="4.5" fill="#ee3036"/><path d="M.5 5h9M5 .5c-2 2.5-2 6.5 0 9M5 .5c2 2.5 2 6.5 0 9" fill="none" stroke="#141414" stroke-width=".7"/></svg>
      </li>
    </ul>

    <div class="person">
      <p class="person__name">Gordon Whitlock</p>
      <address class="person__address">
        482 Tarrow Lane<br>
        Suite 207<br>
        Corvane, GA 30199
      </address>
    </div>
  </section>

  <section class="card card--back" aria-label="Business card back">
    <div class="brand">
      <span class="brand__dot"></span>
      <span class="brand__name">BVEL7K</span>
    </div>
    <p class="website">www.bvel7kga.com</p>
  </section>

</main>
</body>
</html>
```